Inner Compass Podcast W/ Dr. Tom Vane

Podcast Cover Art. I am in search of a re-design for my existing podcast. We have over 100 episodes, but I want to change the name to Inner Compass Podcast With Dr. Tom Vane. I'm open to any ideas, and have attached source file image to use. ( note: NO brain images please).

```html
<!DOCTYPE html>
<html lang="en">
<head>
<meta charset="utf-8">
<title>Inner Compass Podcast With Dr. Tom Vane</title>
<link rel="stylesheet" href="https://fonts.googleapis.com/css2?family=Oswald:wght@500;700&family=Montserrat:wght@800&family=Mrs+Saint+Delafield&display=swap">
<style>
  :root {
    --backdrop: #e6eaf0;
    --ink: #111113;
    --white: #ffffff;
    --coral: #f0613f;
    --deep-red: #c4321f;
    --pill-red: #b0121b;
  }
  html, body {
    margin: 0;
    width: 1200px;
    height: 533px;
    overflow: hidden;
    background: var(--backdrop);
  }
  .stage {
    position: relative;
    width: 1200px;
    height: 533px;
  }
  .cover {
    position: absolute;
    left: 333px;
    top: 0;
    width: 533px;
    height: 533px;
    background: var(--ink);
    overflow: hidden;
  }
  .cover__swash,
  .cover__portrait {
    position: absolute;
    inset: 0;
    width: 533px;
    height: 533px;
  }
  .title-main {
    position: absolute;
    left: 30px;
    top: 26px;
    margin: 0;
    font-family: "Oswald", sans-serif;
    font-weight: 700;
    font-size: 115px;
    line-height: 1;
    letter-spacing: 1px;
    color: var(--white);
  }
  .title-rule {
    position: absolute;
    left: 0;
    top: 148px;
    width: 309px;
    height: 2px;
    background: var(--coral);
  }
  .title-sub {
    position: absolute;
    left: 31px;
    top: 153px;
    margin: 0;
    font-family: "Montserrat", sans-serif;
    font-weight: 800;
    font-size: 31px;
    line-height: 1.2;
    letter-spacing: 0.5px;
    color: var(--coral);
  }
  .network {
    position: absolute;
    left: 342px;
    top: 38px;
    width: 174px;
    height: 80px;
    background: var(--ink);
    display: flex;
    align-items: center;
    gap: 8px;
    padding: 0 10px;
    box-sizing: border-box;
    font-family: "Oswald", sans-serif;
    font-weight: 500;
    color: var(--white);
  }
  .network__dot {
    width: 22px;
    height: 22px;
    border-radius: 50%;
    background: var(--white);
    flex: none;
  }
  .network__name {
    font-size: 19px;
    line-height: 1.1;
    letter-spacing: 0.5px;
  }
  .badge {
    position: absolute;
    left: 82px;
    top: 238px;
    width: 130px;
    height: 32px;
    border-radius: 16px;
    background: var(--white);
    color: var(--pill-red);
    font-family: "Montserrat", sans-serif;
    font-weight: 800;
    font-size: 17px;
    line-height: 32px;
    text-align: center;
  }
  .with {
    position: absolute;
    left: 82px;
    top: 276px;
    width: 130px;
    text-align: center;
    font-family: "Montserrat", sans-serif;
    font-weight: 800;
    font-size: 15px;
    line-height: 18px;
    color: var(--white);
  }
  .host {
    position: absolute;
    left: 34px;
    top: 312px;
    margin: 0;
    font-family: "Mrs Saint Delafield", cursive;
    font-weight: 400;
    font-size: 58px;
    line-height: 1;
    color: var(--white);
    white-space: nowrap;
    transform: rotate(-6deg);
    transform-origin: left center;
  }
</style>
</head>
<body>
<main class="stage">
  <section class="cover">
    <svg class="cover__swash" viewBox="0 0 533 533" aria-hidden="true">
      <defs>
        <linearGradient id="swash-fill" x1="0" y1="1" x2="1" y2="0">
          <stop offset="0" stop-color="#b8301d"/>
          <stop offset="1" stop-color="#f0613f"/>
        </linearGradient>
      </defs>
      <polygon points="0,333 533,138 533,533 0,533" fill="url(#swash-fill)"/>
    </svg>

    <svg class="cover__portrait" viewBox="0 0 533 533" role="img" aria-label="Illustrated portrait of the host in a coral plaid blazer and white checked shirt">
      <defs>
        <linearGradient id="portrait-fill" x1="0" y1="0" x2="0.4" y2="1">
          <stop offset="0" stop-color="#e8714f"/>
          <stop offset="0.6" stop-color="#d9502f"/>
          <stop offset="1" stop-color="#b83520"/>
        </linearGradient>
      </defs>
      <path d="M300,165 Q304,114 370,114 Q438,114 442,170 L445,292 Q515,302 533,322 L533,533 L178,533 Q198,362 292,302 Z" fill="url(#portrait-fill)"/>
    </svg>

    <h1 class="title-main">INNER</h1>
    <div class="title-rule"></div>
    <h2 class="title-sub">COMPASS</h2>

    <div class="network">
      <span class="network__dot"></span>
      <span class="network__name">STEADY GROUND<br>THE PODCAST</span>
    </div>

    <div class="badge">PODCAST</div>
    <div class="with">WITH</div>
    <p class="host">Dr Tom Vane</p>
  </section>
</main>
</body>
</html>
```